依頼詳細
今回初めて募集させていただきます。

依頼は、月刊誌「青嶺」の裏表紙デザインをお願い致します。青嶺されている一般の方は、必ず目にする雑誌です。サイズは【左右154mm×天地232mm】です。尚、2015年10月号(10月1日発刊)に掲載予定です。

当社製品をメインに、シンプルかつ高級感のあるデザインを希望致します。
なんとなくあるイメージは、雑誌によく掲載されているハイブランドの広告のような物を想像していますが、それにとらわれず斬新なものでもかまいません。
ご参考に弊社ホームページをご覧下さい。

今回は「製品紹介」広告ではありませんので、あくまでも企業イメージの浸透をテーマに製作をお願い致します。

尚、写真は約3GB分、こちらの共有ボックス(http://mokubako.jp/box/8TrLw5)においています。添付資料として、弊社ロゴをepsにて、また、2013年に掲載した広告を載せておきます。

よろしくお願い致します。
記載項目
社名:有限会社 朝霧工芸製作所
住所:〒811-1348 福岡市南区桜台7-31-16
電話番号:092-555-3470
FAX:092-555-3475
URL:http://www.asagirikogei.com/
東洋工芸品連合会会員
弊社ロゴ
「初心者用から特註高級品まで」
「カケ」という漢字(常用漢字ではないです、添付の資料2013年9月の広告の中でご確認下さい)
希望イメージ
シンプル 複雑
単色 カラフル
暗い 明るい
日常 高級
遊び心 厳粛
未来的 伝統的
女性的 男性的
希望する色
設定なし
納品ファイル
• イラストレーター形式 (.ai)
補足説明
納品物は
・イラストレータデータ(アウトライン済)
・イラストレータデータ(アウトライン前)+使用しているフォント
いずれも、Adobe illustrator CS6 で編集可能な.aiファイルにてお願い致します。
尚、採用されたデザインの著作権などの権利は、当社に帰属するようにお願致します。
.tifファイルですが、ロゴを追加しました。
フォントの納品、およびアウトライン前のaiデータの納品は、事前に調整に応じていただければ納品しなくて大丈夫です。
本日までに予想をはるかに超える提案をいただいておりまして、なんとも甲乙つけがたしの作品がたくさんあります。

1つは当選作品を選ばせてもらいますが、なんとも惜しいランサーの方の作品に関しては、締め切り後このサイトの直接依頼という形で作品を買い取らせていただきたいと考えています。

買取価格は個別に提示させていただきますので、価格が折り合えばどうぞよろしくお願いいたします。
■ 選んだ理由

「ハイブランドのような」という弊社の思っていたデザインとぴったり一致しました。シンプルかつモノトーンでまとめられ、必要な文言はすべて入っておりまして、弊社職人集団としての力強さをも感じさせてくれました。

■ 提案者全員のお礼・コメント

今回は予想外の数の提案があり、秀逸なデザインばかりでした。誠に有難うございます。次回、傾向とサイズを変えて再び募集いたしますので、その時も是非ご参加をお待ちしています。

```html
<!DOCTYPE html>
<html lang="ja">
<head>
<meta charset="utf-8">
<title>朝霧工芸製作所 裏表紙広告</title>
<link rel="stylesheet" href="https://fonts.googleapis.com/css2?family=Noto+Serif+JP:wght@400;600;700;900&display=swap">
<style>
  :root {
    --bg: #2d2725;
    --panel: #eaa53f;
    --ink: #3a281d;
    --headline: #ffffff;
    --kanji: #d9d4cd;
    --photo-light: #e9cf97;
    --photo-mid: #c99f58;
    --photo-dark: #8a6634;
  }
  * { margin: 0; padding: 0; box-sizing: border-box; }
  html, body { width: 798px; height: 1200px; overflow: hidden; background: var(--bg); }
  .ad {
    position: relative;
    width: 798px;
    height: 1200px;
    background: var(--bg);
    font-family: "Noto Serif JP", serif;
    overflow: hidden;
  }
  .hero-photo { position: absolute; left: 0; top: 0; }
  .headline {
    position: absolute;
    top: 10px;
    left: 24px;
    writing-mode: vertical-rl;
    color: var(--headline);
    font-weight: 900;
    font-size: 56px;
    line-height: 1.0;
    letter-spacing: 0.02em;
    height: 200px;
  }
  .kake-mark {
    position: absolute;
    right: 22px;
    top: 560px;
    color: var(--kanji);
    font-weight: 400;
    font-size: 200px;
    line-height: 1;
  }
  .info-panel {
    position: absolute;
    left: 22px;
    top: 763px;
    width: 756px;
    height: 422px;
    background: var(--panel);
    color: var(--ink);
    text-align: center;
  }
  .tagline {
    position: absolute;
    top: 28px;
    width: 100%;
    font-size: 27px;
    font-weight: 600;
    letter-spacing: 0.18em;
  }
  .membership {
    position: absolute;
    top: 88px;
    left: 240px;
    width: 276px;
    height: 34px;
    border: 2px solid var(--ink);
    font-size: 19px;
    line-height: 30px;
    font-weight: 600;
    letter-spacing: 0.06em;
  }
  .brand-dot {
    position: absolute;
    top: 148px;
    left: 356px;
    width: 44px;
    height: 44px;
    border-radius: 50%;
    background: var(--ink);
  }
  .company-type {
    position: absolute;
    top: 222px;
    width: 100%;
    font-size: 18px;
    font-weight: 600;
    letter-spacing: 0.1em;
  }
  .company-name {
    position: absolute;
    top: 246px;
    width: 100%;
    font-size: 40px;
    font-weight: 700;
    letter-spacing: 0.08em;
  }
  .contact {
    position: absolute;
    top: 306px;
    width: 100%;
    font-size: 16px;
    line-height: 23px;
    letter-spacing: 0.03em;
  }
</style>
</head>
<body>
<main class="ad">
  <svg class="hero-photo" width="798" height="763" viewBox="0 0 798 763" role="img" aria-label="弓道用のカケ（弓懸）の接写写真。紫の紐と刺繍が施された鹿革の手袋">
    <defs>
      <radialGradient id="photoTone" cx="0.45" cy="0.4" r="0.65">
        <stop offset="0" stop-color="var(--photo-light)"/>
        <stop offset="0.6" stop-color="var(--photo-mid)"/>
        <stop offset="1" stop-color="var(--photo-dark)"/>
      </radialGradient>
    </defs>
    <circle cx="430" cy="330" r="400" fill="url(#photoTone)"/>
  </svg>

  <h1 class="headline">職人の<br>技術で<br>完璧。</h1>

  <div class="kake-mark">弽</div>

  <section class="info-panel">
    <p class="tagline">初心者用から　特註高級品まで</p>
    <p class="membership">東洋工芸品連合会会員</p>
    <span class="brand-dot" aria-hidden="true"></span>
    <p class="company-type">有限会社</p>
    <p class="company-name">朝霧工芸製作所</p>
    <p class="contact">
      〒811-1348　福岡市南区桜台7-31-16<br>
      TEL:092-555-3470　FAX:092-555-3475<br>
      http://www.asagirikogei.com/
    </p>
  </section>
</main>
</body>
</html>
```